Supplement Bottle Label Greens Revised

We want to design a front label for a health supplement bottle. The product is called Meadow Sip Chews™. This will be a new product so there is no current website for the product. However it will be bundled with the product attached Belly Poise.
We want it to be modern, vibrant and appealing.
Bottle size: standard size supplement CLEAR bottle size, with white child resistant cap and the label panel dimensions are 3” x 7”. The label should be primarily white and green, with a touch of red; (see color palettes)/it can also ONLY be white and green. It should complement the Belly Poise bottle when it’s right next to it.
We are only focused on the front of the bottle design, not on the back, but leave space for the supplement panel and other text on the back.
So the text for the front of the bottle is:
RW Talbot's
Meadow Sip Chews™
Super Greens Blend for:
Energy, Digestion, and Immune Support*
60 Gummies | Dietary Supplement
Raspberry Flavor Gummies
Off to side of the label:
Non-GMO
Vegan Friendly
Plant-Based
Gelatin Free

```html
<!DOCTYPE html>
<html lang="en">
<head>
<meta charset="utf-8">
<title>Meadow Sip Chews™ – Raspberry Flavor Gummies Label</title>
<link href="https://fonts.googleapis.com/css2?family=Roboto+Condensed:wght@300;400;700&display=swap" rel="stylesheet">
<style>
  :root {
    --backdrop: #dcdcdc;
    --leaf-green: #1f6b24;
    --leaf-green-deep: #0f5314;
    --label-white: #ffffff;
    --berry-red: #b3172b;
    --berry-red-bright: #d23a52;
    --ink: #1e1e1e;
    --claim-green: #3e8a2c;
    --list-green: #4b9a3a;
  }
  html, body {
    margin: 0;
    padding: 0;
    width: 1200px;
    height: 1200px;
    overflow: hidden;
    background: var(--backdrop);
  }
  .canvas {
    position: relative;
    width: 1200px;
    height: 1200px;
  }
  .front-label {
    position: absolute;
    left: 100px;
    top: 100px;
    width: 1000px;
    height: 1000px;
    font-family: "Roboto Condensed", "Arial Narrow", sans-serif;
  }
  .badge-text { font-weight: 700; font-size: 54px; fill: var(--label-white); letter-spacing: 1px; }
  .brand-name { font-weight: 700; font-size: 58px; fill: var(--ink); }
  .flavor-word { font-weight: 700; font-size: 96px; fill: var(--berry-red); }
  .flavor-tag { font-weight: 700; font-size: 92px; fill: var(--label-white); }
  .format-word { font-weight: 700; font-size: 66px; fill: var(--ink); }
  .claim-lead { font-weight: 700; font-size: 42px; fill: var(--claim-green); }
  .benefit-item { font-weight: 300; font-size: 35px; fill: var(--list-green); }
  .benefit-tick { fill: none; stroke: var(--list-green); stroke-width: 4; stroke-linecap: round; stroke-linejoin: round; }
</style>
</head>
<body>
<main class="canvas">
  <svg class="front-label" viewBox="0 0 1000 1000" xmlns="http://www.w3.org/2000/svg" aria-label="Meadow Sip Chews front label">
    <defs>
      <linearGradient id="band-shade" x1="0" x2="1" y1="0" y2="0">
        <stop offset="0" stop-color="var(--leaf-green-deep)"/>
        <stop offset="0.5" stop-color="var(--leaf-green)"/>
        <stop offset="1" stop-color="var(--leaf-green-deep)"/>
      </linearGradient>
      <linearGradient id="badge-shade" x1="0" x2="1" y1="0" y2="0">
        <stop offset="0" stop-color="var(--berry-red-bright)"/>
        <stop offset="1" stop-color="var(--berry-red)"/>
      </linearGradient>
      <radialGradient id="berry-shade" cx="0.45" cy="0.55" r="0.6">
        <stop offset="0" stop-color="#d8263a"/>
        <stop offset="0.6" stop-color="#c9243a"/>
        <stop offset="0.85" stop-color="#6ea83c"/>
        <stop offset="1" stop-color="#ffffff" stop-opacity="0"/>
      </radialGradient>
    </defs>

    <!-- green wrap -->
    <rect class="label-band" x="0" y="0" width="1000" height="1000" fill="url(#band-shade)"/>
    <!-- white centre panel with inward curved sides -->
    <path class="label-panel" fill="var(--label-white)"
      d="M10 78 L990 78 Q895 505 990 935 L10 935 Q100 505 10 78 Z"/>

    <!-- purity badge -->
    <path class="purity-badge" fill="url(#badge-shade)"
      d="M119 0 L424 0 L410 200 Q408 229 380 229 L150 229 Q122 229 120 200 Z"/>
    <text class="badge-text" x="269" y="66" text-anchor="middle">NATURAL</text>
    <text class="badge-text" x="269" y="135" text-anchor="middle">100%</text>
    <text class="badge-text" x="269" y="204" text-anchor="middle">PURE</text>

    <!-- product name -->
    <text class="brand-name" x="452" y="146">Meadow Sip</text>
    <text class="brand-name" x="643" y="208" text-anchor="middle">Chews™</text>
    <line class="brand-rule" x1="486" y1="230" x2="800" y2="228" stroke="var(--berry-red)" stroke-width="3"/>

    <!-- flavor line -->
    <text class="flavor-word" x="127" y="328">Raspberry</text>
    <rect class="flavor-box" x="553" y="254" width="265" height="94" fill="var(--berry-red)"/>
    <text class="flavor-tag" x="563" y="338">Flavor</text>
    <text class="format-word" x="127" y="407">Gummies</text>

    <!-- claims -->
    <text class="claim-lead" x="100" y="465">Super Greens Blend for:</text>
    <g class="benefit-list">
      <path class="benefit-tick" d="M110 506 l7 8 l14 -16"/><text class="benefit-item" x="142" y="516">60 Gummies | Dietary Supplement</text>
      <path class="benefit-tick" d="M110 547 l7 8 l14 -16"/><text class="benefit-item" x="142" y="557">Digestion</text>
      <path class="benefit-tick" d="M110 588 l7 8 l14 -16"/><text class="benefit-item" x="142" y="598">Immune</text>
      <path class="benefit-tick" d="M112 629 l7 8 l14 -16"/><text class="benefit-item" x="140" y="639">Energy</text>
      <path class="benefit-tick" d="M112 670 l7 8 l14 -16"/><text class="benefit-item" x="140" y="680">Immune Support</text>
      <path class="benefit-tick" d="M110 711 l7 8 l14 -16"/><text class="benefit-item" x="146" y="721">Vegan Friendly</text>
      <path class="benefit-tick" d="M108 752 l7 8 l14 -16"/><text class="benefit-item" x="143" y="762">Plant-Based</text>
      <path class="benefit-tick" d="M108 793 l7 8 l14 -16"/><text class="benefit-item" x="143" y="803">Gelatin Free</text>
      <path class="benefit-tick" d="M108 834 l7 8 l14 -16"/><text class="benefit-item" x="142" y="844">Non-GMO</text>
      <path class="benefit-tick" d="M108 875 l7 8 l14 -16"/><text class="benefit-item" x="141" y="885">Plant-Based</text>
    </g>

    <!-- fruit artwork area -->
    <rect class="fruit-art" x="442" y="545" width="464" height="357" rx="150" fill="url(#berry-shade)"
      role="img" aria-label="Three ripe raspberries with green leaves"/>
  </svg>
</main>
</body>
</html>
```